business card design for a small scale specialty cut flower farm

We need a business card design for Hollowmere Bloom Farm based in Langley, BC, Canada. We produce specialty, high-end cut flowers and sell locally to florists, local shops and markets and the end user through bouquet subscriptions. The final business card design should be memorable and have a timeless or vintage feel. We would prefer a square shape.
Updates

Target Market(s)

florists, shops and seasonal markets, local flower lovers

Industry/Entity Type

Floral

Contact Information for Business Card

Tamsin Ellery Voss, Grower
Langley, BC, Canada
website: hollowmerebloomfarm.example
instagram: @hollowmerebloomfarm
Tel: 555.317.4290
facebook: www.facebook.example/hollowmereblooms/

Font styles to use
Serif
Decorative
Script

Requirements
Must have
• soft black background colour on front side, the included logo and catch phrase: Fresh Local Seasonal
Nice to have
• phone number and website address on front of card, included photo 6539 incorporated onto the back, possibly photo 6609 as well.

```html
<!DOCTYPE html>
<html lang="en">
<head>
<meta charset="utf-8">
<title>Hollowmere Bloom Farm – Business Card</title>
<link href="https://fonts.googleapis.com/css2?family=Allura&family=Lato:wght@400&family=Roboto:wght@400&display=swap" rel="stylesheet">
<style>
  :root {
    --page-bg: #e6e2dd;
    --card-bg: #252322;
    --ink: #f1ece6;
    --ink-soft: #d9d3cc;
    --muted: #9c968f;
    --rule: #4a4644;
    --rose: #e8b5c3;
    --rose-deep: #c9718d;
    --leaf: #4f6f3c;
    --leaf-light: #dfe8d2;
    --social-blue: #4f86a8;
    --icon-grey: #a8a498;
  }
  * { box-sizing: border-box; margin: 0; padding: 0; }
  html, body {
    width: 1200px;
    height: 1054px;
    overflow: hidden;
    background: var(--page-bg);
  }
  .business-card {
    position: absolute;
    left: 200px;
    top: 127px;
    width: 800px;
    height: 800px;
    background: var(--card-bg);
    border-radius: 20px;
    overflow: hidden;
    box-shadow: 0 10px 30px rgba(0,0,0,0.18);
  }
  .brand {
    position: absolute;
    left: 0;
    top: 70px;
    width: 800px;
    text-align: center;
  }
  .brand-dot {
    display: block;
    width: 76px;
    height: 76px;
    margin: 0 auto 24px;
    border-radius: 50%;
    background: var(--rose);
  }
  .brand-name {
    font-family: "Lato", sans-serif;
    font-weight: 400;
    font-size: 28px;
    line-height: 1.35;
    letter-spacing: 0.22em;
    text-transform: uppercase;
    color: var(--ink);
  }
  .brand-est {
    margin-top: 14px;
    font-family: "Lato", sans-serif;
    font-size: 13px;
    letter-spacing: 0.32em;
    color: var(--muted);
  }
  .divider {
    position: absolute;
    left: 300px;
    top: 330px;
    width: 200px;
    height: 1px;
    background: var(--rule);
  }
  .contact-block {
    position: absolute;
    left: 0;
    top: 356px;
    width: 800px;
    text-align: center;
  }
  .person-name {
    font-family: "Allura", cursive;
    font-size: 56px;
    line-height: 1.1;
    color: var(--ink);
  }
  .person-role {
    margin-top: 6px;
    font-family: "Roboto", sans-serif;
    font-size: 21px;
    color: var(--ink-soft);
  }
  .contact-list {
    display: inline-block;
    list-style: none;
    margin-top: 34px;
    text-align: left;
  }
  .contact-item {
    display: flex;
    align-items: center;
    height: 36px;
    font-family: "Roboto", sans-serif;
    font-size: 22px;
    color: var(--ink-soft);
  }
  .contact-icon {
    width: 20px;
    height: 20px;
    margin-right: 22px;
    flex: none;
  }
  .bottom-bands {
    position: absolute;
    left: 0;
    bottom: 0;
    width: 800px;
    height: 72px;
  }
  .tagline {
    position: absolute;
    right: 70px;
    bottom: 16px;
    font-family: "Allura", cursive;
    font-size: 36px;
    line-height: 1;
    color: var(--leaf-light);
  }
</style>
</head>
<body>
  <div class="business-card">
    <div class="brand">
      <span class="brand-dot" aria-hidden="true"></span>
      <div class="brand-name">Hollowmere<br>Bloom Farm</div>
      <div class="brand-est">EST.2019</div>
    </div>

    <div class="divider" aria-hidden="true"></div>

    <div class="contact-block">
      <div class="person-name">Tamsin Ellery Voss</div>
      <div class="person-role">Grower</div>
      <ul class="contact-list">
        <li class="contact-item">
          <svg class="contact-icon" viewBox="0 0 24 24" aria-hidden="true">
            <path d="M6.6 10.8a15 15 0 0 0 6.6 6.6l2.2-2.2a1 1 0 0 1 1-.25 11.4 11.4 0 0 0 3.6.57 1 1 0 0 1 1 1V20a1 1 0 0 1-1 1A17 17 0 0 1 3 4a1 1 0 0 1 1-1h3.5a1 1 0 0 1 1 1c0 1.25.2 2.45.57 3.57a1 1 0 0 1-.25 1z" fill="var(--icon-grey)"/>
          </svg>
          (555) 317-4290
        </li>
        <li class="contact-item">
          <svg class="contact-icon" viewBox="0 0 24 24" aria-hidden="true">
            <g fill="none" stroke="var(--icon-grey)" stroke-width="1.6">
              <circle cx="12" cy="12" r="9.5"/>
              <ellipse cx="12" cy="12" rx="4.2" ry="9.5"/>
              <line x1="2.5" y1="12" x2="21.5" y2="12"/>
              <line x1="4" y1="7" x2="20" y2="7"/>
              <line x1="4" y1="17" x2="20" y2="17"/>
            </g>
          </svg>
          hollowmerebloomfarm.example
        </li>
        <li class="contact-item">
          <svg class="contact-icon" viewBox="0 0 24 24" aria-hidden="true">
            <circle cx="12" cy="12" r="10" fill="var(--rose-deep)"/>
          </svg>
          @hollowmerebloomfarm
        </li>
        <li class="contact-item">
          <svg class="contact-icon" viewBox="0 0 24 24" aria-hidden="true">
            <circle cx="12" cy="12" r="10" fill="var(--social-blue)"/>
          </svg>
          /hollowmereblooms
        </li>
      </ul>
    </div>

    <svg class="bottom-bands" viewBox="0 0 800 72" aria-hidden="true">
      <rect x="0" y="50" width="330" height="22" fill="var(--rose)"/>
      <path d="M303 72 C330 30 340 0 372 0 L800 0 L800 72 Z" fill="var(--leaf)"/>
    </svg>
    <div class="tagline">Fresh Local Seasonal</div>
  </div>
</body>
</html>
```